Digital Imaging Website Design Project

This project is for 3 page designs - The main Home page design, department page design & content page design which will utilize most of the home page components.

Client Background - http://www.kelrofab.com

An almost Forty year old established printing company that has a large client base of architect/engineering, as the print shop opened up as a blueprinting company, and over the years has grown, changed and expanded to offer document and digital file management for this industry. KRFab. has also always offered color printing services, but recently has expanded their color department to be able to offer amazing dimensional printing, and extreme cutting technology.

These new products and services will be targeted to new industries for repeatable printing needs, promotional, point of purchase color printing, as well as in-store, interior decor/wall. These new printing services are only offered by KRFAB in their area, and they want to convey that they are on the leading edge of color printing technology, while at the same time, not eliminating their existing primary business scaring away their traditional client base of architectural/engineering firms that use them for large format printing, scanning and document management services.

1 - Home Page Design
Primary Goals of the design:

1.Provide a new, eye catching engaging website that conveys the above expansion/growth/cutting edge company.
2.Full screen design please to move away from the 'center' bordered up website they currently have.
3.Design Components – We don't have any media to provide you with exception of our logo. We're looking for fresh design that is exciting and engaging imagery. Additionally, we are working on a color/effected version of our logo to place on the color division page, and this will probably tie in with the design you create for us.
4.It should be designed to be able to work as a responsive design as well so that when installed, will work across devices etc..
5.Colors – Same color scheme, but if you have an accent color you'd like to use to make the site pop, go for it!

Requirements:
1.The 4 divisions of the company should be the main feature so that the client depending on which department they are needing, will see those 4 choices clearly in the design, and they'll know to click on one of them to get more information and to their needed services.

2.The main goal of the site is to get visitors to place an order, there should be a feature on the home page for this call to action.

3.Put in an element that communicates the main benefit of KRFab. - an area for a 1-line Statement/Call to Action / Overall Company Benefit/

4.The 4 divisions need to have eye catching elements related to their products and services, and that clearly illustrate that the user should click on that to go to the appropriate area for products and services

Reprographics
This department is specifically geared to architect/engineering industry
BYLine for optional Use: Partnering with Building Industry Providers since 1975
Related pages for better understanding:
http://www.kelrofab.com/services/portland_professional_printing_services
http://www.kelrofab.com/services/reprographics
Digital File Management
This department is related to Architect/engineers, but can also apply to any other industry needing electronic document management, scanning, or archival services.
BYLine for optional use: Effective & Efficient Digital Solutions at every level.
Related Pages:
http://www.kelrofab.com/colorgraphics/electronic_file_document_management
http://www.kelrofab.com/colorgraphics/document_scanning_service
http://www.kelrofab.com/services/scanning_and_archiving

Color Graphics
This Department is newly expanded / has expanded services / they are focusing more of their efforts on this department and is a key reason for updated website design.
This Department image/representation should be stellar in the imagery to convey the excellence of the color department the services availble.
One of their newest products/services is dimensional printing – not 3-D, but raised element printing. Essentially a client could pick components on their graphic that that they want to 'bump' out, and additional layers would be put in place to create a popped out, dimensional effect. * Bonus points for creating the color department image that effectively conveys this new service – whether it's showing an abstract image/element that is actually raised off the page/paper/component. Additionally the color dimensional printing can be done on practically any material – glass, vinyl, material etc.... Please let me know if you have any questions on this.
BYLine for optional Use: See How Our Color Stands Out From the Rest
Related pages:
http://www.kelrofab.com/colorgraphics
http://www.kelrofab.com/colorgraphics/color_digital_imaging

Equipment & Supplies
This department provides specific supplies and hardware vs. printing products/services. Our largest client base is architects/engineers, but is not limited to this industry. Typical equipment is large printers, and supplies are typically paper products geared to the large format printing services, for the architect/engineers industry.
Byline for optional Use: In-House Printing & Fulfillment Services
Related pages:
http://www.kelrofab.com/varlen_tusk_equipment_sales
http://www.kelrofab.com/supplies

Additionally - Possibly have descriptive text sections below these 4 elements, but this is optional.

2.) Department/Division Page design -

This page should pull the home page element to over based on which division is selected.
Have a submenu design incorporated so that users can navigate to all the products and services that will be listed under that division
Contain a plugin design for FAQs – so that depending on which division page they are on, the appropriate FAQ's would display for use to have easy access to.
Contain a plugin design for – Contact Us easy form – short form –
Name
Company
Number
Email
Project Details/Questions: Text box

3.)Content Page design
This page should have main area for content
Area for an image with slideshow of other supporting images
Optional area for video – most (99%) of the pages will not have videos, but in the case we do, would like an area that will display videos effectively.
Optional FAQ plugin display
Contact plugin display

Global Elements:

Static and very visible site features that are in a position so that if user clicks beyond home page will still see these are:
Get a Quote
Place Order
Digital Plan-room
Call Today - 503-481-7962

Other global components:
SM Icons – QN, Chirpo, WorkLoop
Rotating Testimonial

Navigational Menu:
The KRF Difference
About
Sustainability
Products & Services
Reprograhics
Digital File Management
Color Graphics
Equipment & Supplies
Login
Blog
Contact Us

After the contest – What would be great to have is when a user clicks on one of the departments, it takes that visual element and continues onto it's department page for a smaller but related image - But this may be an after this web design contest.

Additionally will need some other design work on the interior pages, as well, so hoping to find a great designer to complete the other tasks – as well as be the go-to for future endeavors!

Thanks for looking at the project, and I look forward to any questions you may have.
Updates

Looking forward to hearing from interested designers! - If you're curious about my work, you can find my profile at:  https://www.gigmarla.com/users/~07b3e2f95d18c4a260

Target Market(s)

Please see description

Industry/Entity Type

Electronic

Requirements
Must have
• Please see description

```html
<!DOCTYPE html>
<html lang="en">
<head>
<meta charset="utf-8">
<title>KRF Digital Imaging</title>
<link href="https://fonts.googleapis.com/css2?family=Ubuntu:wght@300;400;500;700&display=swap" rel="stylesheet">
<style>
:root{
  --purple:#4a4a9e;
  --purple-dark:#3f3f8a;
  --nav:#3a3a3a;
  --orange:#f7b81c;
  --red:#ee4a4a;
  --dark:#343434;
  --darker:#2d2d2d;
  --bottom:#222222;
  --light:#efefef;
  --muted:#9a9a9a;
  --white:#ffffff;
}
*{margin:0;padding:0;box-sizing:border-box}
html,body{width:1200px;height:2384px;overflow:hidden}
body{font-family:'Ubuntu',sans-serif;background:var(--white);position:relative;color:#333}
.abs{position:absolute}

/* header */
.site-header{left:0;top:0;width:1200px;height:121px;background:var(--purple)}
.brand{left:188px;top:34px;display:flex;align-items:center;gap:14px;color:var(--white)}
.brand-mark{width:44px;height:44px;border-radius:50%;background:var(--white)}
.brand-name{font-weight:700;font-size:15px;line-height:17px;letter-spacing:.5px;text-transform:uppercase}
.brand-name small{display:block;font-weight:700;font-size:15px}
.top-links{right:172px;top:11px;display:flex;gap:14px;font-size:11px;color:var(--white)}
.order-btn{left:795px;top:64px;width:235px;height:45px;background:var(--orange);border-radius:3px;color:#2b2b2b;font-weight:500;font-size:17px;display:flex;align-items:center;justify-content:center;gap:12px;white-space:nowrap}

.main-nav{left:0;top:121px;width:1200px;height:47px;background:var(--nav);display:flex;align-items:center;padding-left:173px}
.main-nav a{color:var(--white);text-decoration:none;font-size:13px;margin-right:28px;white-space:nowrap}

/* hero */
.hero{left:0;top:178px;width:1200px;height:534px;background:linear-gradient(100deg,#1e9a52 0%,#8cc63f 18%,#e8d32a 35%,#f5c21d 52%,#f08a1c 68%,#e9344e 85%,#e64a8c 100%)}
.hero-band{left:0;top:712px;width:1200px;height:8px;background:var(--purple)}
.hero-caption{left:332px;top:459px;width:685px;height:221px;background:rgba(45,45,45,.85);padding:18px 20px}
.hero-title{font-size:44px;line-height:52px;color:var(--white);font-weight:500;letter-spacing:-.5px;display:flex;align-items:center;gap:12px;white-space:nowrap}
.hero-title span{flex-shrink:0}
.hero-title .light{font-weight:300}
.hero-title .tag{background:var(--purple);padding:0 12px;font-weight:700}
.hero-text{margin-top:10px;font-size:13px;line-height:21px;color:#dcdcdc}
.hero-text b{color:var(--white)}
.read-more{margin-top:14px;width:145px;height:41px;background:var(--red);color:var(--white);font-size:15px;display:flex;align-items:center;justify-content:center;gap:12px}

/* divisions */
.divisions{left:0;top:720px;width:1200px;height:375px;background:var(--light)}
.division{top:720px;width:199px;height:257px;background:var(--white);box-shadow:0 4px 0 #dcdcdc;text-align:center}
.division-icon{height:133px;background:var(--purple);display:flex;align-items:center;justify-content:center}
.division h3{font-size:14px;font-weight:500;margin-top:22px;color:#333;white-space:nowrap}
.division hr{width:150px;margin:16px auto 14px;border:0;border-top:1px solid #e6e6e6}
.division p{font-size:12px;color:#b0b0b0;line-height:17px}
.leaf-badge{left:551px;top:1042px;width:96px;height:96px;border-radius:50%;background:var(--dark);display:flex;align-items:flex-start;justify-content:center;padding-top:20px}

/* portfolio */
.portfolio{left:0;top:1095px;width:1200px;height:767px;background:var(--dark)}
.port-lead{top:1194px;font-size:13px;color:#d8d8d8}
.port-lead b{color:var(--white)}
.port-title{left:466px;top:1168px;width:270px;height:72px;background:var(--purple);color:var(--white);font-size:42px;font-weight:500;display:flex;align-items:center;justify-content:center;letter-spacing:-1px}
.work{top:1303px;width:271px;height:318px;background:#2a2a2a;box-shadow:0 3px 0 #242424;text-align:center}
.work-img{height:181px}
.work h3{color:var(--white);font-weight:500;font-size:20px;margin-top:14px}
.work hr{width:200px;margin:16px auto 14px;border:0;border-top:1px solid #3f3f3f}
.work p{font-size:12px;color:#bdbdbd;line-height:19px;padding:0 20px}
.divider{left:172px;top:1683px;width:856px;border-top:1px solid #3e3e3e}
.quote{left:172px;top:1709px;width:630px;font-size:12px;line-height:19px;color:#d4d4d4}
.quote b{color:var(--white)}
.quote .cite{color:var(--red)}
.testimonial-btn{left:855px;top:1716px;width:172px;height:48px;background:var(--red);color:var(--white);font-size:13px;font-weight:500;display:flex;align-items:center;justify-content:center}

/* footer */
.footer{left:0;top:1862px;width:1200px;height:458px;background:var(--darker)}
.notch{left:589px;top:1862px;width:0;height:0;border-left:11px solid transparent;border-right:11px solid transparent;border-top:11px solid var(--dark)}
.col-head{top:1924px;display:flex;align-items:center;gap:20px;color:var(--white);font-size:18px;font-weight:500;text-transform:uppercase;width:273px;border-bottom:1px solid #3d3d3d;padding-bottom:6px;white-space:nowrap}
.col-icon{width:40px;height:46px;background:var(--purple);display:flex;align-items:center;justify-content:center;flex-shrink:0}
.about-text{left:172px;top:1987px;width:270px;font-size:12px;line-height:18px;color:#b5b5b5}
.about-text p{margin-bottom:18px}
.contact-line{display:flex;align-items:center;gap:12px;color:#777;margin-bottom:4px}
.contact-line i{width:10px;height:10px;background:#555;display:inline-block}
.equip{width:132px;height:81px;background:linear-gradient(135deg,#e9e9ee,#b8bcc6)}
.news{left:757px;width:270px;font-size:12px;line-height:18px;color:#c8c8c8;border-bottom:1px solid #3d3d3d;padding-bottom:8px}
.news a{color:var(--red);text-decoration:none}
.news em{display:block;color:#808080;font-size:11px}

.bottom-bar{left:0;top:2320px;width:1200px;height:64px;background:var(--bottom);display:flex;align-items:center;padding:0 172px;font-size:12px;color:#bbb}
.bottom-bar .tag{background:var(--purple);color:var(--white);padding:4px 8px;margin:0 10px}
.bottom-bar em{color:#9a9a9a}
.social{margin-left:auto;display:flex;gap:14px}
.social span{width:16px;height:16px;border-radius:50%;background:#e0e0e0}
</style>
</head>
<body>

<header class="abs site-header">
  <div class="abs brand"><span class="brand-mark"></span><div class="brand-name">Kelro Fabrication<small>Company, Inc.</small></div></div>
  <nav class="abs top-links"><span>Login</span><span>Blog</span><span>Contact Us</span><span>About Us</span></nav>
  <div class="abs order-btn"><span>Order Now</span><span>1-800-642-3170</span></div>
</header>
<nav class="abs main-nav">
  <a>The KRF Difference</a><a>Sustainability</a><a>Products &amp; Services</a><a>Reprograhics</a><a>Digital File Management</a><a>Color Graphics</a><a>Equipment &amp; Supplies</a>
</nav>

<section class="abs hero" role="img" aria-label="Fanned colour swatch cards in a rainbow arc"></section>
<div class="abs hero-band"></div>
<div class="abs hero-caption">
  <h1 class="hero-title"><span>Lorem Ipsum.</span><span class="light">Faux</span><span class="tag">simplement</span></h1>
  <p class="hero-text"><b>Lorem Ipsum est simplement</b> du faux texte employé dans la sition et la misen page avant impression. Le Lorem Ipsum est le faux texte standard de l'imprimerie depuis les années 1500, quand un peintre anonyme assembla ensemble des <b>morceaux de texte pour réaliser un livre spécimen</b> de polices de texte.</p>
  <div class="read-more"><svg width="16" height="13" viewBox="0 0 16 13"><rect x="0" y="3" width="16" height="10" rx="1" fill="#fff"/><rect x="5" y="0" width="6" height="4" fill="none" stroke="#fff" stroke-width="1.5"/></svg>Read More</div>
</div>

<section class="abs divisions"></section>
<div class="abs division" style="left:172px">
  <div class="division-icon"><svg width="70" height="70" viewBox="0 0 70 70" fill="none" stroke="#fff" stroke-width="3"><rect x="10" y="8" width="14" height="48" rx="7"/><rect x="28" y="8" width="14" height="48" rx="7"/><rect x="46" y="8" width="14" height="48" rx="7"/><path d="M10 50l7 12 7-12M28 50l7 12 7-12M46 50l7 12 7-12"/></svg></div>
  <h3>Graphic Imaging Services</h3><hr><p>texte employé dans la sition<br>misen page avant</p>
</div>
<div class="abs division" style="left:391px">
  <div class="division-icon"><svg width="74" height="74" viewBox="0 0 74 74" fill="none" stroke="#fff"><circle cx="37" cy="37" r="33" stroke-width="5"/><circle cx="37" cy="37" r="22" stroke-width="5"/><circle cx="37" cy="37" r="8" fill="#fff"/></svg></div>
  <h3>Lastest Digital Technology</h3><hr><p>texte employé dans la sition<br>misen page avant</p>
</div>
<div class="abs division" style="left:611px">
  <div class="division-icon"><svg width="76" height="76" viewBox="0 0 76 76"><circle cx="34" cy="42" r="30" fill="#fff"/><g fill="#4a4a9e"><circle cx="34" cy="26" r="7"/><circle cx="34" cy="58" r="7"/><circle cx="18" cy="42" r="7"/><circle cx="50" cy="42" r="7"/><circle cx="34" cy="42" r="3"/></g><path d="M52 16l18-12" stroke="#fff" stroke-width="5"/></svg></div>
  <h3>Digital Film Management</h3><hr><p>texte employé dans la sition<br>misen page avant</p>
</div>
<div class="abs division" style="left:831px">
  <div class="division-icon"><svg width="60" height="76" viewBox="0 0 60 76"><rect x="2" y="2" width="56" height="72" fill="#fff"/><rect x="10" y="10" width="40" height="56" fill="none" stroke="#4a4a9e" stroke-width="2" stroke-dasharray="3 3"/><rect x="18" y="30" width="24" height="14" fill="none" stroke="#4a4a9e" stroke-width="3"/><path d="M18 36h24" stroke="#4a4a9e" stroke-width="2"/></svg></div>
  <h3>Reprographics Service</h3><hr><p>texte employé dans la sition<br>misen page avant</p>
</div>

<section class="abs portfolio"></section>
<div class="abs leaf-badge"><svg width="30" height="26" viewBox="0 0 30 26"><path d="M3 24C3 10 12 3 28 2 27 17 18 24 6 20" fill="#fff"/><path d="M3 24L16 11" stroke="#343434" stroke-width="2"/></svg></div>
<p class="abs port-lead" style="left:214px">We work hard to <b>impress people.</b></p>
<h2 class="abs port-title">PORTFOLIO</h2>
<p class="abs port-lead" style="left:803px">Why not check <b>our hard work?</b></p>

<article class="abs work" style="left:172px"><div class="work-img" role="img" aria-label="Rolled architectural blueprints on a technical drawing" style="background:linear-gradient(135deg,#d6dde6,#8a9bb0)"></div><h3>Lorem Ipsum est</h3><hr><p>The whole of science is nothing more than a refinement of everyday thinking.</p></article>
<article class="abs work" style="left:464px"><div class="work-img" role="img" aria-label="Fanned rainbow colour swatch book" style="background:linear-gradient(120deg,#e23b3b,#f3c224,#3cae5a,#2a7fd0,#a23ad0)"></div><h3>Simplement du faux</h3><hr><p>The whole of science is nothing more than a refinement of everyday thinking.</p></article>
<article class="abs work" style="left:757px"><div class="work-img" role="img" aria-label="Stack of patterned printed vinyl sheets" style="background:linear-gradient(135deg,#f05a9a,#3fb6e0 50%,#d23a3a)"></div><h3>Texte employé dans la</h3><hr><p>The whole of science is nothing more than a refinement of everyday thinking.</p></article>

<div class="abs divider"></div>
<p class="abs quote">“<b>Lorem Ipsum est simplement</b> du faux texte employé dans la sition et la misen page avant impression. Le Lorem Ipsum est le faux texte standard de l'imprimerie depuis les années 1500, quand un peintre anonyme assembla ensemble des <b>morceaux de texte pour réaliser un livre spécimen</b> de polices de texte.” &nbsp;<span class="cite">fait que survivre</span></p>
<div class="abs testimonial-btn">View All Testimonials</div>

<footer class="abs footer"></footer>
<div class="abs notch"></div>

<div class="abs col-head" style="left:172px"><span class="col-icon"><svg width="14" height="12"><path d="M0 1h14M0 6h14M0 11h14" stroke="#fff" stroke-width="2"/></svg></span>About Us</div>
<div class="abs about-text">
  <p>He who joyfully marches to music rank and file, has already earned my contempt. He has been given a large brain by mistake, since for him the spinal cord would surely suffice.</p>
  <p>This disgrace to civilization should be done away with at once. Heroism at command, how violently I hate all this, how despicable and ignoble war is.</p>
  <div class="contact-line"><i></i>Cedar Falls, UT 84021</div>
  <div class="contact-line"><i></i>(871) 555-0142</div>
  <div class="contact-line"><i></i>hello@krfab-mail.com</div>
</div>

<div class="abs col-head" style="left:464px"><span class="col-icon"><svg width="14" height="12"><path d="M0 1h14M0 6h14M0 11h14" stroke="#fff" stroke-width="2"/></svg></span>Equipment for Sale</div>
<div class="abs equip" role="img" aria-label="Large format printer" style="left:463px;top:1993px"></div>
<div class="abs equip" role="img" aria-label="Offset press" style="left:600px;top:1993px"></div>
<div class="abs equip" role="img" aria-label="Roll printing machine" style="left:463px;top:2079px"></div>
<div class="abs equip" role="img" aria-label="Screen printing machine" style="left:600px;top:2079px"></div>
<div class="abs equip" role="img" aria-label="Industrial press line" style="left:463px;top:2165px"></div>
<div class="abs equip" role="img" aria-label="Flatbed printer" style="left:600px;top:2165px"></div>

<div class="abs col-head" style="left:757px"><span class="col-icon"><svg width="14" height="12"><path d="M0 1h14M0 6h14M0 11h14" stroke="#fff" stroke-width="2"/></svg></span>Recent News</div>
<div class="abs news" style="top:1989px">I love this awesome freebie that you my brand new can check @ <a>http://t.co/4kmRq2x</a><em>About 15 mins</em></div>
<div class="abs news" style="top:2082px">Check out my brand new webdesign my brand new released @ <a>http://t.co/4kmRq2x</a><em>About 2 days</em></div>
<div class="abs news" style="top:2175px">I love this awesome freebie that you my brand new can check @ <a>http://t.co/4kmRq2x</a><em>About 3 months</em></div>

<div class="abs bottom-bar">Copyright 2013 <span class="tag">KRF Digital Image</span><em>// The super duper awesome digital agency.</em>
  <div class="social"><span></span><span></span><span></span><span></span><span></span><span></span></div>
</div>

</body>
</html>
```